label design for oral care product

Kindly invite you to design bottle label (114 mm*40 mm) for our product, a kind of oral care product. The GEL is different from our previous cleanser product, as the pic we uploaded for demonstration. The color of frosted glass bottle is dark green, but the cap is white. You could download the pic of bottle among the uploaded files. The logo file and label content description are attached too. Please check them. Our product is made from many kinds of natural plant extracts, which includes herb and fruit. I wish the label would make our product look high-end and reliable. And it would be better if you could give some advice on paper material and special requirements for printing, related to your design. I value the texture of label too, because I think that stands for the quality of products. No color limitation for the use of our logo.
20-40 female, who value oral health.

```html
<!DOCTYPE html>
<html lang="en">
<head>
<meta charset="utf-8">
<title>Velvi Mint Aligner Gel – Label</title>
<link rel="stylesheet" href="https://fonts.googleapis.com/css2?family=Arimo:wght@400;700&family=Righteous&family=Roboto+Slab:wght@700&display=swap">
<style>
  :root {
    --backdrop: #d3d3d3;
    --gold: #e0a623;
    --gold-deep: #cf931a;
    --green: #2f7a1f;
    --green-dark: #246316;
    --paper: #ffffff;
    --ink: #3a3a3a;
    --leaf-light: #e4efdc;
    --leaf-mid: #b7d3a6;
  }
  * { margin: 0; padding: 0; box-sizing: border-box; }
  html, body {
    width: 1200px;
    height: 900px;
    overflow: hidden;
    background: var(--backdrop);
  }
  .canvas {
    position: relative;
    width: 1200px;
    height: 900px;
  }
  .label {
    position: absolute;
    left: 330px;
    top: 97px;
    width: 540px;
    height: 705px;
    background: var(--paper);
    display: flex;
    flex-direction: column;
    box-shadow: 0 10px 30px rgba(0,0,0,0.12);
  }
  .brand-band {
    height: 261px;
    background: radial-gradient(circle at 50% 45%, var(--gold) 0%, var(--gold-deep) 100%);
    display: flex;
    align-items: center;
    justify-content: center;
    gap: 18px;
  }
  .brand-mark {
    width: 30px;
    height: 30px;
    border-radius: 50%;
    background: #fff;
  }
  .brand-name {
    font-family: "Righteous", sans-serif;
    font-size: 66px;
    color: #fff;
    line-height: 1;
    letter-spacing: 1px;
  }
  .accent-stripe {
    height: 45px;
    background: var(--green);
  }
  .info-panel {
    flex: 1;
    position: relative;
    display: flex;
    flex-direction: column;
    align-items: center;
    padding-top: 44px;
    text-align: center;
  }
  .product-name {
    font-family: "Righteous", sans-serif;
    font-size: 46px;
    line-height: 1;
    letter-spacing: 2px;
  }
  .product-name .word-aligner { color: var(--gold); }
  .product-name .word-gel { color: var(--green); }
  .product-tagline {
    font-family: "Arimo", sans-serif;
    font-size: 28px;
    color: var(--ink);
    margin-top: 8px;
    padding-bottom: 14px;
    position: relative;
  }
  .product-tagline::after {
    content: "";
    position: absolute;
    left: 50%;
    bottom: 0;
    width: 120px;
    height: 3px;
    transform: translateX(-50%);
    background: var(--gold);
  }
  .product-claim {
    font-family: "Arimo", sans-serif;
    font-size: 23px;
    color: var(--ink);
    margin-top: 16px;
  }
  .product-benefit {
    font-family: "Roboto Slab", serif;
    font-weight: 700;
    font-size: 40px;
    color: var(--green);
    margin-top: 8px;
    letter-spacing: 0.5px;
  }
  .net-weight {
    font-family: "Arimo", sans-serif;
    font-weight: 700;
    font-size: 19px;
    color: #fff;
    background: var(--gold);
    border-radius: 18px;
    padding: 7px 34px;
    margin-top: 22px;
    position: relative;
    z-index: 1;
  }
  .botanical-strip {
    position: absolute;
    left: 0;
    right: 0;
    bottom: 0;
    height: 80px;
    background: linear-gradient(180deg, rgba(255,255,255,0) 0%, var(--leaf-light) 45%, var(--leaf-mid) 100%);
  }
</style>
</head>
<body>
  <main class="canvas">
    <section class="label">
      <header class="brand-band">
        <span class="brand-mark"></span>
        <span class="brand-name">Velvi Mint</span>
      </header>
      <div class="accent-stripe"></div>
      <div class="info-panel">
        <h1 class="product-name"><span class="word-aligner">ALIGNER</span> <span class="word-gel">GEL</span></h1>
        <p class="product-tagline">Immune Support for Oral Health</p>
        <p class="product-claim">the Solution to Maintain Dental Hygiene and</p>
        <p class="product-benefit">STRENGTHEN GUMS</p>
        <p class="net-weight">net weight-30 ml / 1 fl oz</p>
        <div class="botanical-strip" role="img" aria-label="Soft green herb and leaf illustration along the bottom edge"></div>
      </div>
    </section>
  </main>
</body>
</html>
```